We need a designer to help us represent our unique approach to creating lesson plans for digital learning. At the Autumn Gathering for Online Fluency, held in Providence RI this July 13 - 18, we'll use your design with 100 teachers and then put it online to reach hundreds of thousands more.

We have a draft visual of our model that we like - but it's not pretty (Since we are not designers, it looks a little clunky).

Please create a simple and attractive design in two versions: (1) one that we can use as a 1-page printed handout and (2) one that we can use where teachers can fill in sections and write ideas under each section of the graphic.

Why you should bid on this job? We're a leading provider of digital and media literacy curriculum resources with a huge international and national audience. Working with us will establish your expertise in the area of educational multimedia design.

Target Market(s)

Elementary and secondary teachers in public schools

Industry/Entity Type

Digital

Font styles to use
Sans Serif

Requirements
Must have
• TITLE : Digital Literacy Curriculum Framework

1 page version - suitable for use as a poster or 1-page flyer

Fillable form version - suitable for use as a handout with spaces for teachers to write

```html
<!DOCTYPE html>
<html lang="en">
<head>
<meta charset="utf-8">
<title>Digital Literacy Curriculum Framework</title>
<link rel="stylesheet" href="https://fonts.googleapis.com/css2?family=Open+Sans:wght@400;600&display=swap">
<style>
  :root {
    --paper: #f4f3e6;
    --ring: #e2dfb1;
    --ring-line: #ffffff;
    --brown: #7b6650;
    --brown-light: #a28d72;
    --axis: #8a7660;
    --self: #fdcb9b;
    --learners: #f9a64a;
    --community: #a8c3b4;
    --context: #fcd667;
    --subject: #44a6b0;
    --white: #ffffff;
  }
  html, body {
    margin: 0;
    padding: 0;
    overflow: hidden;
    background: var(--paper);
  }
  .framework {
    position: relative;
    width: 848px;
    height: 1200px;
    overflow: hidden;
    background: var(--paper);
    font-family: "Open Sans", Arial, sans-serif;
  }
  .framework-graphic {
    position: absolute;
    inset: 0;
  }
  .banner-title {
    font-size: 27px;
    font-weight: 400;
    fill: var(--white);
    letter-spacing: 0.5px;
  }
  .segment-label {
    font-size: 20px;
    fill: var(--brown);
    letter-spacing: 1px;
  }
  .quadrant-label {
    font-size: 19px;
    fill: var(--white);
  }
  .subject-label {
    font-size: 20px;
    fill: var(--white);
  }
  .corner-label {
    position: absolute;
    margin: 0;
    font-size: 20px;
    font-weight: 400;
    color: var(--brown);
    letter-spacing: 0.5px;
    line-height: 1;
  }
  .corner-purpose { left: 88px; top: 132px; }
  .corner-assessment { right: 56px; top: 139px; }
  .corner-content { left: 83px; top: 1130px; }
  .corner-pedagogy { right: 56px; top: 1136px; }
</style>
</head>
<body>
<main class="framework">
  <svg class="framework-graphic" width="848" height="1200" viewBox="0 0 848 1200" aria-labelledby="framework-title">
    <defs>
      <path id="outer-label-path" d="M425,269 A355,355 0 1 1 425,979 A355,355 0 1 1 425,269"/>
      <path id="inner-label-path" d="M425,439 A185,185 0 1 1 425,809 A185,185 0 1 1 425,439"/>
    </defs>

    <!-- title banner -->
    <g class="banner">
      <polygon class="banner-tail" points="31,44 96,44 96,94 31,94 46,69" fill="var(--brown-light)"/>
      <polygon class="banner-tail" points="817,44 752,44 752,94 817,94 802,69" fill="var(--brown-light)"/>
      <rect class="banner-band" x="88" y="31" width="672" height="52" fill="var(--brown)"/>
      <text id="framework-title" class="banner-title" x="424" y="67" text-anchor="middle">DIGITAL LITERACY CURRICULUM FRAMEWORK</text>
    </g>

    <!-- axes -->
    <g class="axes" stroke="var(--axis)" stroke-width="1.5">
      <line x1="425" y1="128" x2="425" y2="222"/>
      <line x1="425" y1="1026" x2="425" y2="1200"/>
      <line x1="0" y1="624" x2="23" y2="624"/>
      <line x1="827" y1="624" x2="848" y2="624"/>
    </g>

    <!-- outer ring -->
    <circle class="outer-ring" cx="425" cy="624" r="403" fill="var(--ring)" stroke="var(--brown-light)" stroke-width="1.5"/>
    <g class="ring-dividers" stroke="var(--ring-line)" stroke-width="1.5">
      <line x1="300" y1="445" x2="194" y2="294"/>
      <line x1="556" y1="450" x2="668" y2="302"/>
      <line x1="638" y1="669" x2="819" y2="708"/>
      <line x1="425" y1="842" x2="425" y2="1027"/>
      <line x1="213" y1="673" x2="32" y2="715"/>
    </g>

    <g class="segment-labels">
      <text class="segment-label" text-anchor="middle" dominant-baseline="middle"><textPath href="#outer-label-path" startOffset="0%">STANDARDS</textPath></text>
      <text class="segment-label" text-anchor="middle" dominant-baseline="middle"><textPath href="#outer-label-path" startOffset="19.5%">WORK PRODUCTS</textPath></text>
      <text class="segment-label" text-anchor="middle" dominant-baseline="middle"><textPath href="#outer-label-path" startOffset="39.5%">INSTRUCTIONAL STRATEGIES</textPath></text>
      <text class="segment-label" text-anchor="middle" dominant-baseline="middle"><textPath href="#outer-label-path" startOffset="60.3%">TOOLS</textPath></text>
      <text class="segment-label" text-anchor="middle" dominant-baseline="middle"><textPath href="#outer-label-path" startOffset="80.5%">TEXT</textPath></text>
      <text class="segment-label" text-anchor="middle" dominant-baseline="middle"><textPath href="#outer-label-path" startOffset="100%">STANDARDS</textPath></text>
    </g>

    <!-- inner quadrants -->
    <g class="quadrants">
      <path class="quadrant-self" d="M425,624 L207,624 A218,218 0 0 1 425,406 Z" fill="var(--self)"/>
      <path class="quadrant-learners" d="M425,624 L425,406 A218,218 0 0 1 643,624 Z" fill="var(--learners)"/>
      <path class="quadrant-community" d="M425,624 L643,624 A218,218 0 0 1 425,842 Z" fill="var(--community)"/>
      <path class="quadrant-context" d="M425,624 L425,842 A218,218 0 0 1 207,624 Z" fill="var(--context)"/>
      <g stroke="var(--ring-line)" stroke-width="1.5">
        <line x1="207" y1="624" x2="643" y2="624"/>
        <line x1="425" y1="406" x2="425" y2="842"/>
      </g>
    </g>

    <g class="quadrant-labels">
      <text class="quadrant-label" text-anchor="middle" dominant-baseline="middle"><textPath href="#inner-label-path" startOffset="88.3%">Self</textPath></text>
      <text class="quadrant-label" text-anchor="middle" dominant-baseline="middle"><textPath href="#inner-label-path" startOffset="13.9%">Learners</textPath></text>
      <text class="quadrant-label" text-anchor="middle" dominant-baseline="middle"><textPath href="#inner-label-path" startOffset="35.3%">Community</textPath></text>
      <text class="quadrant-label" text-anchor="middle" dominant-baseline="middle"><textPath href="#inner-label-path" startOffset="61.4%">Context</textPath></text>
    </g>

    <!-- subject hub -->
    <circle class="subject-ring" cx="425" cy="624" r="91" fill="none" stroke="var(--brown)" stroke-width="1.2"/>
    <circle class="subject-hub" cx="425" cy="624" r="81" fill="var(--subject)"/>
    <text class="subject-label" x="425" y="631" text-anchor="middle">SUBJECT</text>
  </svg>

  <h2 class="corner-label corner-purpose">PURPOSE</h2>
  <h2 class="corner-label corner-assessment">ASSESMENT</h2>
  <h2 class="corner-label corner-content">CONTENT</h2>
  <h2 class="corner-label corner-pedagogy">PEDAGOGY</h2>
</main>
</body>
</html>
```